Car rental website design for a UAE car rental company

This project is about creating a new website design for a car rental company located in Dubai (United Arab Emirates), I opened the same project a few months ago but I didn't receive a lot of appealing entries so I closed it but this time I am marking the project as guaranteed to avoid such situation again, if you have already provided a design before then please re-submit again on this project so that it is considered while reviewing all the designs

A few important things:

1- We need a simple non-complex design
2- The final deliverable would be 2 screens (PSD, JPEG ... etc), the first screen is for the home page and the second screen is for an internal page
3- The home page must have a section that end users can use to rent a car online directly from the home page instead of going into some inner pages
4- The current website is very old and not very appealing so avoid creating a similar design (www.quarvin-drive.example)
5- The name is Quarvin but the company rents normal cars (no Limousin cars will be rented) so avoid adding any fancy cars in the images/graphics used in the design, just normal end users cars
6- The expected pages would be: home, About us, Our team, Strategy, Contact us and links to social media pages
7- The attachments include the company's logo and some screens from other car rental companies that provide online rentals/payments

If you have any questions please feel free to ask and please note that we will need the designs urgently

Thanks

Target Market(s)

Dubai - United Arab Emirates

Industry/Entity Type

It Company

Number of Pages Required

2 page

Font styles to use
Sans Serif

Requirements
Must have
• Check the project details
Nice to have
Should not have

```html
<!DOCTYPE html>
<html lang="en">
<head>
<meta charset="utf-8">
<title>Quarvin – Car Rental in Dubai</title>
<link rel="stylesheet" href="https://fonts.googleapis.com/css2?family=Ubuntu:ital,wght@0,400;0,500;0,700;1,500&family=Arimo:wght@400;700&display=swap">
<style>
:root{
  --crimson:#a8123e;
  --crimson-dark:#8c0d33;
  --ink:#1f1f1f;
  --text:#3a3a3a;
  --muted:#6d6d6d;
  --line:#c9c9c9;
  --paper:#ffffff;
  --mist:#f3f3f3;
  --nav-active:#7f9086;
  --charcoal:#2c2c2c;
  --footer:#232323;
  --footer-text:#d9d9d9;
}
*{box-sizing:border-box;margin:0;padding:0}
html,body{width:961px;height:1200px;overflow:hidden}
body{position:relative;background:var(--paper);font-family:"Arimo",Arial,sans-serif;color:var(--text)}
.abs{position:absolute}

/* header */
.topline{left:0;top:0;width:961px;height:4px;background:var(--crimson)}
.header{left:0;top:4px;width:961px;height:65px;background:var(--paper);border-bottom:1px solid var(--line)}
.brand{display:flex;align-items:center;gap:7px}
.brand-mark{width:22px;height:22px;background:var(--crimson)}
.brand-name{font-family:"Ubuntu",sans-serif;font-weight:500;color:var(--nav-active)}
.header .brand{position:absolute;left:248px;top:18px}
.header .brand-name{font-size:22px}
.nav{position:absolute;left:477px;top:0;height:64px;display:flex;font-family:"Ubuntu",sans-serif;font-size:10px;color:#444}
.nav a{color:inherit;text-decoration:none;display:flex;align-items:center;padding:0 6px}
.nav a.active{background:var(--nav-active);color:#fff;width:33px;justify-content:center;padding:0}

/* hero */
.hero{left:0;top:69px;width:961px;height:307px;background:linear-gradient(100deg,#f1f1f1 0%,#ececec 40%,#e4e6ea 60%,#f4f4f4 100%)}
.hero-photo{left:420px;top:75px;width:400px;height:300px;background:radial-gradient(ellipse at 60% 40%,#e8e9ed 0%,#dedfe3 40%,rgba(240,240,240,0) 72%)}
.hero-title{left:451px;top:86px;font-family:"Ubuntu",sans-serif;font-weight:500;font-size:21px;color:#111}

.rent{left:246px;top:112px;width:198px;height:260px;background:rgba(255,255,255,.93);border:1px solid #cfcfcf;border-radius:4px;overflow:hidden}
.rent-head{height:29px;background:var(--crimson);color:#fff;font-family:"Arimo",sans-serif;font-weight:700;font-size:14px;display:flex;align-items:center;justify-content:center;letter-spacing:.2px}
.rent-body{padding:8px 7px 0;font-size:7.5px;color:#333}
.field-label{margin-top:4px;margin-bottom:5px}
.row{display:flex;gap:5px;margin-bottom:9px}
.select{height:16px;border:1px solid #bdbdbd;background:#fff;font-size:6px;color:#999;display:flex;align-items:center;justify-content:space-between;padding:0 4px}
.select::after{content:"";border:2px solid transparent;border-top:3px solid #333;margin-top:3px}
.w-date{width:95px}.w-time{width:38px}.w-full{width:182px}
.gap-lg{margin-top:14px}
.rent-note{margin-top:4px}
.rent-link{display:block;margin-top:5px;font-weight:700;color:var(--crimson)}
.btn-quote{display:inline-block;margin-top:6px;background:linear-gradient(#d23a68,var(--crimson));color:#fff;font-weight:700;font-size:7.5px;padding:6px 9px;border-radius:2px}

/* welcome */
.welcome{left:0;top:376px;width:961px;height:102px;background:var(--paper);text-align:center}
.section-title{font-family:"Arimo",sans-serif;font-weight:700;font-size:13.5px;color:#1a1a1a;letter-spacing:.3px}
.welcome .section-title{margin-top:16px}
.lead{margin-top:7px;font-size:8px;color:var(--crimson)}
.body-copy{margin:4px auto 0;width:470px;font-size:8px;line-height:11px;color:#222}
.btn-solid{display:inline-block;margin-top:6px;background:var(--crimson);color:#fff;font-size:8px;padding:3px 11px;border-radius:2px}

/* how it works */
.how{left:0;top:478px;width:961px;height:129px;background:var(--mist)}
.how .section-title{position:absolute;top:9px;width:100%;text-align:center}
.step{position:absolute;top:30px;width:110px;text-align:center}
.step-icon{width:37px;height:37px;border-radius:50%;background:var(--crimson);border:2px solid #e9b7c5;margin:0 auto;display:flex;align-items:center;justify-content:center}
.step-name{margin-top:6px;font-size:8px;color:#222}
.step-copy{margin-top:3px;font-size:6.8px;line-height:9.5px;color:#777}
.btn-outline{display:inline-block;margin-top:4px;border:1px solid var(--crimson);color:var(--crimson);font-size:6.5px;padding:1px 6px;border-radius:2px;background:#fff}

/* gallery */
.gallery{left:0;top:607px;width:961px;height:121px;background:var(--paper)}
.gallery .section-title{position:absolute;left:452px;top:9px}
.arrows{position:absolute;display:flex;gap:2px}
.arrow{width:10px;height:10px;display:flex;align-items:center;justify-content:center}
.arrow.prev{background:#4a4a4a}.arrow.next{background:var(--crimson)}
.thumb{position:absolute;top:36px;width:110px;height:75px;border:1px solid #9a9a9a;padding:2px;background:#fff}
.thumb span{display:block;width:100%;height:100%}

/* promos */
.promo{top:738px;width:240px;height:112px;color:#fff;text-align:center}
.promo-phone{left:240px;background:linear-gradient(90deg,#b2164a,#a01240)}
.promo-offers{left:480px;background:linear-gradient(90deg,#3a3a3a,#262626)}
.promo h3{margin-top:21px;font-family:"Arimo",sans-serif;font-weight:400;font-size:14px}
.promo p{margin:8px auto 0;width:200px;font-size:7.5px;line-height:9.5px}
.btn-ghost{display:inline-block;margin-top:8px;border:1px solid #fff;font-size:7.5px;padding:3px 11px}

/* testimonials */
.testimonials{left:0;top:860px;width:961px;height:190px;background:var(--mist)}
.testimonials .section-title{position:absolute;left:428px;top:9px}
.quote{position:absolute;left:320px;top:54px;width:320px;text-align:center;font-size:7.8px;line-height:10px;color:#222}
.qmark{position:absolute;font-family:Georgia,serif;font-weight:700;font-size:24px;color:var(--crimson);line-height:1}
.author{position:absolute;left:407px;top:130px;font-family:"Ubuntu",sans-serif;font-style:italic;font-weight:500;font-size:8.5px;color:var(--crimson)}
.avatar{position:absolute;left:513px;top:103px;width:64px;height:64px;border-radius:50%;border:2px solid var(--crimson);background:#fff;padding:3px}
.avatar span{display:block;width:100%;height:100%;border-radius:50%;background:linear-gradient(#d9d9d9,#b9bcc0)}

/* footer */
.footer{left:0;top:1050px;width:961px;height:138px;background:linear-gradient(90deg,#202020,#2d2d2d 50%,#1f1f1f)}
.footer .brand{position:absolute;left:272px;top:60px}
.footer .brand-name{font-size:20px;color:#c9cec9}
.fcol{position:absolute;top:30px;font-family:"Ubuntu",sans-serif;color:var(--footer-text)}
.fcol h4{font-weight:400;font-size:9.5px;color:#fff;margin-bottom:9px}
.fnav{list-style:none;border-left:1px solid #555;padding-left:9px;font-size:7.5px;line-height:17.5px}
.fnav li::before{content:"•";margin-right:6px}
.contact{display:flex;align-items:center;gap:8px;font-size:8px;margin-bottom:9px}
.signup{display:flex;margin-top:2px}
.signup .input{width:62px;height:12px;background:#fff;color:#999;font-size:5.5px;padding-left:3px;display:flex;align-items:center}
.signup .go{height:12px;background:var(--crimson);color:#fff;font-size:5.5px;padding:0 3px;display:flex;align-items:center}
.social{display:flex;gap:3px}
.social span{width:13px;height:13px;border-radius:50%;background:#6f6f6f}
.social span:nth-child(even){background:var(--crimson)}
.bottombar{left:0;top:1188px;width:961px;height:12px;background:var(--crimson)}
.copyright{left:251px;top:1190px;font-size:5px;color:#e7a7b8}
</style>
</head>
<body>

<div class="abs topline"></div>
<header class="abs header">
  <div class="brand"><span class="brand-mark"></span><span class="brand-name">Quarvin</span></div>
  <nav class="nav">
    <a class="active" href="#">Home</a>
    <a href="#">About us</a>
    <a href="#">Our team</a>
    <a href="#">Strategy</a>
    <a href="#">Contact us</a>
  </nav>
</header>

<section class="abs hero"></section>
<div class="abs hero-photo" role="img" aria-label="Toy model cars in blue, white and red behind a set of car keys on a white surface"></div>
<h1 class="abs hero-title">Find a car rental in Dubai</h1>

<form class="abs rent">
  <div class="rent-head">RENT A CAR</div>
  <div class="rent-body">
    <div class="field-label">Rental start Date/Time</div>
    <div class="row"><span class="select w-date">2015-04-4</span><span class="select w-time">10AM</span><span class="select w-time">03PM</span></div>
    <div class="field-label">Rental End Date/Time</div>
    <div class="row"><span class="select w-date">2015-04-4</span><span class="select w-time">10AM</span><span class="select w-time">05PM</span></div>
    <div class="field-label gap-lg">Pickup Location</div>
    <div class="row"><span class="select w-full">Location</span></div>
    <div class="field-label">Returning Location</div>
    <div class="row"><span class="select w-full">Location</span></div>
    <div class="rent-note">Can't find location you're looking for?</div>
    <span class="rent-link">View Map</span>
    <span class="btn-quote">GET A QUOTE</span>
  </div>
</form>

<section class="abs welcome">
  <h2 class="section-title">WELCOME</h2>
  <p class="lead">As Dubai is expected to welcome millions of tourists and visitors, car rental industry is believed to escalate more rapidly in the region.</p>
  <p class="body-copy">Lorem Ipsum is simply dummy text of the printing and typesetting industry. Lorem Ipsum has been the industry's standard dummy text ever since the 1500s, when an unknown printer took a galley of type and scrambled.</p>
  <span class="btn-solid">MORE</span>
</section>

<section class="abs how">
  <h2 class="section-title">HOW IT WORKS</h2>
  <div class="step" style="left:282px">
    <div class="step-icon"><svg width="20" height="20" viewBox="0 0 20 20" fill="none" stroke="#fff" stroke-width="2"><circle cx="8" cy="8" r="5"/><path d="M12 12l5 5"/></svg></div>
    <div class="step-name">Find a car</div>
    <div class="step-copy">It is a long established fact<br>that a reader will be...</div>
    <span class="btn-outline">More</span>
  </div>
  <div class="step" style="left:425px">
    <div class="step-icon"><svg width="20" height="20" viewBox="0 0 20 20" fill="none" stroke="#fff" stroke-width="2"><rect x="3" y="3" width="14" height="14" rx="3"/><path d="M6.5 10l2.5 2.5 5-5"/></svg></div>
    <div class="step-name">Book it</div>
    <div class="step-copy">It is a long established fact<br>that a reader will be...</div>
    <span class="btn-outline">More</span>
  </div>
  <div class="step" style="left:571px">
    <div class="step-icon"><svg width="22" height="20" viewBox="0 0 22 20" fill="#fff"><circle cx="4" cy="4" r="2.2"/><rect x="2.3" y="7" width="3.4" height="9" rx="1"/><path d="M9 10l2-4h7l2 4v5H9z"/><circle cx="12" cy="15.5" r="1.6" fill="var(--crimson)"/><circle cx="17.5" cy="15.5" r="1.6" fill="var(--crimson)"/></svg></div>
    <div class="step-name">Pick it Up</div>
    <div class="step-copy">It is a long established fact<br>that a reader will be...</div>
    <span class="btn-outline">More</span>
  </div>
</section>

<section class="abs gallery">
  <h2 class="section-title">GALLERY</h2>
  <div class="arrows" style="left:692px;top:12px">
    <span class="arrow prev"><svg width="6" height="6" viewBox="0 0 6 6"><path d="M4 0.5L1.5 3 4 5.5" stroke="#fff" fill="none"/></svg></span>
    <span class="arrow next"><svg width="6" height="6" viewBox="0 0 6 6"><path d="M2 0.5L4.5 3 2 5.5" stroke="#fff" fill="none"/></svg></span>
  </div>
  <div class="thumb" style="left:247px"><span role="img" aria-label="Red compact sedan" style="background:linear-gradient(#f4f4f4 30%,#b51d2a 55%,#eeeeee 80%)"></span></div>
  <div class="thumb" style="left:366px"><span role="img" aria-label="Silver family sedan" style="background:linear-gradient(#f6f6f6 30%,#a9adb1 55%,#eeeeee 80%)"></span></div>
  <div class="thumb" style="left:486px"><span role="img" aria-label="Orange coupe parked by the sea" style="background:linear-gradient(#aac3d6 20%,#c9662a 55%,#8f8f8f 85%)"></span></div>
  <div class="thumb" style="left:606px"><span role="img" aria-label="White sedan parked beside trees" style="background:linear-gradient(#6f8f55 20%,#f2f2f2 55%,#9a9a9a 85%)"></span></div>
</section>

<section class="abs promo promo-phone">
  <h3>Book a car rental with your phone</h3>
  <p>Lorem Ipsum is simply dummy text of the printing and typesetting industry. Lorem Ipsum has been the industry's standard dummy text .</p>
  <span class="btn-ghost">MORE</span>
</section>
<section class="abs promo promo-offers">
  <h3>Special Offers and packages</h3>
  <p>Lorem Ipsum is simply dummy text of the printing and typesetting industry. Lorem Ipsum has been the industry's standard dummy text .</p>
  <span class="btn-ghost">MORE</span>
</section>

<section class="abs testimonials">
  <h2 class="section-title">TESTIMONIALS</h2>
  <div class="arrows" style="left:692px;top:11px">
    <span class="arrow prev"><svg width="6" height="6" viewBox="0 0 6 6"><path d="M4 0.5L1.5 3 4 5.5" stroke="#fff" fill="none"/></svg></span>
    <span class="arrow next"><svg width="6" height="6" viewBox="0 0 6 6"><path d="M2 0.5L4.5 3 2 5.5" stroke="#fff" fill="none"/></svg></span>
  </div>
  <span class="qmark" style="left:318px;top:48px">“</span>
  <p class="quote">Lorem ipsum dolor sit amet, consectetur adipiscing elit, sed do eiusmod tempor incididunt ut labore et dolore magna aliqua. Ut enim ad minim veniam, quis nostrud exercitation ullamco laboris.</p>
  <span class="qmark" style="left:551px;top:80px">”</span>
  <span class="author">Mr. Dalen physiotherapist</span>
  <div class="avatar"><span role="img" aria-label="Portrait photo of the customer"></span></div>
</section>

<footer class="abs footer" role="contentinfo">
  <div class="brand"><span class="brand-mark"></span><span class="brand-name">Quarvin</span></div>
  <div class="fcol" style="left:399px">
    <h4>Quick Navigation</h4>
    <ul class="fnav"><li>Home</li><li>About us</li><li>Our team</li><li>Strategy</li></ul>
  </div>
  <div class="fcol" style="left:515px">
    <h4>Get in touch</h4>
    <div class="contact"><svg width="10" height="10" viewBox="0 0 10 10" fill="#fff"><path d="M2 0.5l2 2-1 1.3c.6 1.3 1.6 2.3 2.9 2.9l1.3-1 2 2-1.3 1.6C4.6 9.3.7 5.4.4 1.8z"/></svg>+971 4 555 0182</div>
    <div class="contact"><svg width="12" height="9" viewBox="0 0 12 9" fill="none" stroke="#fff"><rect x="0.5" y="0.5" width="11" height="8"/><path d="M0.5 0.5l5.5 4.5 5.5-4.5"/></svg>info@quarvin-drive.example</div>
    <div class="signup"><span class="input">Email address</span><span class="go">SIGN UP</span></div>
  </div>
  <div class="fcol" style="left:642px">
    <h4>Follow Us</h4>
    <div class="social"><span></span><span></span><span></span><span></span></div>
  </div>
</footer>
<div class="abs bottombar"></div>
<div class="abs copyright">Copyright © 2007-2015 Quarvin. All rights reserved.</div>

</body>
</html>
```